Scuba diving website (Only 1 page. If nice all website later for you)

The payment is for one page only. We are looking for the main design of our new website. For test you will have to redesign the page that is attached to this description. If we like the style we will choose you as the main designer for the whole website (around 20 pages).
The website is about scuba diving. It targets world wide in 4 languages dive centers, divers, underwater photographers, dive sites research, fish species info many more to come. The website is bulid on strong fondation and expect high visits. Developpment is done.
We need now to find the perfect design. The page to redesign is a page about a "dive center" that subscribe to the website where he presents himself and fills it's information. (like a plimbook page).
We are looking for between MODERN and MINIMAL design, but most of all a CLEAN design. See below some design website we like
http://velorint.com/pathe/
http://www.quandrell.com/
http://www.paltravex.com/
http://widgets.tarnimello.com/
For the color stay around the blue and orange. The page width should be 1024px.
Updates
You can use small diving pictures for presenting the "Neighbouring dive sites" in the page. (instead of the red and white flag)
Target Market(s)
We target people willing to go on holiday for diving. We target photographer, cameraman who wants to share picture of their dive, we target people who have an interest for fish species (they can tag more than 32000 different species on their picture/video). We target dive centers who want to advertise on the website by creating their own page

```html
<!DOCTYPE html>
<html lang="en">
<head>
<meta charset="utf-8">
<title>Divora Diving Center</title>
<link href="https://fonts.googleapis.com/css2?family=Open+Sans:wght@400;600;700&display=swap" rel="stylesheet">
<style>
:root{
  --navy:#0c2a50;
  --navy-2:#12386a;
  --blue:#1c63ad;
  --sky:#e9f3fb;
  --orange:#f28a1b;
  --orange-d:#d9730c;
  --ink:#333a42;
  --muted:#8a929b;
  --line:#dfe4ea;
  --star:#f5a623;
  --foot:#1e2125;
  --foot-2:#15171a;
}
*{box-sizing:border-box;margin:0;padding:0}
html,body{width:1200px;height:3396px;overflow:hidden}
body{position:relative;background:#fff;font-family:"Open Sans",Arial,sans-serif;color:var(--ink);font-size:13px}
.abs{position:absolute}
.wrap{left:112px;width:976px}

/* header */
.header{left:0;top:0;width:1200px;height:380px;background:linear-gradient(var(--navy),var(--navy-2))}
.brand{left:120px;top:18px;color:#fff}
.brand-name{font-size:40px;font-weight:600;line-height:44px;letter-spacing:.5px}
.brand-sub{font-size:11px;color:var(--orange);letter-spacing:2px;font-weight:600;text-transform:uppercase}
.top-actions{right:112px;top:22px;display:flex;gap:8px}
.btn-top{height:26px;padding:0 16px;line-height:26px;font-size:12px;color:#fff;border-radius:2px;background:#24497a}
.btn-top.primary{background:var(--orange)}
.nav{left:112px;top:110px;display:flex;height:42px}
.nav a{display:block;padding:0 20px;line-height:42px;color:#fff;font-size:13px;font-weight:600;text-decoration:none;text-transform:uppercase}
.nav a.active{background:#fff;color:var(--blue);border-top:3px solid var(--orange);line-height:39px}
.hero{top:152px;height:448px;border:6px solid #fff;background:linear-gradient(100deg,#d9a930 0%,#c07b2a 14%,#1d8aa8 30%,#12729a 60%,#0b4f7e 100%);box-shadow:0 2px 6px rgba(0,0,0,.15)}

/* section headings */
.sec-title{font-size:19px;font-weight:700;color:var(--blue)}
.sec-title small{font-size:11px;color:var(--muted);font-weight:400}
.rule{height:1px;background:var(--line)}
.like{display:inline-flex;align-items:center;gap:4px;height:18px;padding:0 6px;border:1px solid #c6ccd6;background:#f4f6f9;font-size:10px;color:#44516a;border-radius:2px}
.like i{display:inline-block;width:10px;height:10px;background:#44516a;border-radius:2px}
.btn{display:inline-block;height:32px;line-height:32px;padding:0 18px;background:var(--orange);color:#fff;font-size:12px;font-weight:600;border-radius:2px;border-bottom:2px solid var(--orange-d)}
.photo{border-radius:2px}

/* info */
.info-grid .label{color:var(--muted);width:100px;display:inline-block}
.info-row{height:24px;line-height:24px;font-size:13px}
.info-row a{color:var(--orange);text-decoration:underline}
.flag{display:inline-block;width:18px;height:12px;margin-right:4px;vertical-align:middle}
.stars{display:inline-flex;gap:2px;vertical-align:middle}
.rate-row{display:flex;justify-content:space-between;height:24px;line-height:24px}

/* facilities */
.fac-list{list-style:none}
.fac-list li{height:26px;line-height:26px;padding-left:14px;position:relative;color:#58616b}
.fac-list li:before{content:"";position:absolute;left:0;top:11px;width:5px;height:5px;background:var(--orange);border-radius:50%}

/* tabs & gallery */
.tabs{display:flex;height:36px;border-bottom:1px solid var(--line)}
.tab{padding:0 18px;line-height:35px;font-size:13px;color:var(--muted);background:#f3f5f8;border:1px solid var(--line);border-bottom:none;margin-right:4px}
.tab.active{background:#fff;color:var(--blue);font-weight:700;margin-bottom:-1px;height:36px}
.g-card{width:304px}
.g-card .photo{height:188px}
.meta{font-size:10px;color:var(--muted);margin:10px 0 6px;display:flex;justify-content:space-between}
.g-title{font-weight:700;font-size:13px;margin-bottom:6px}
.g-text{font-size:12px;color:#6a727b;line-height:18px}

/* dive sites */
.site{width:470px;height:196px;border:1px solid var(--line);padding:14px;display:flex;gap:18px}
.site .photo{width:170px;height:166px;flex:none}
.site-name{color:var(--orange);font-weight:700;font-size:14px;margin-bottom:6px}
.site-row{height:24px;line-height:24px;font-size:12px;color:#5c646d}
.site-row b{font-weight:400;color:var(--muted);display:inline-block;width:80px}
.link{color:var(--blue);font-size:11px}

/* reviews */
.reviews{left:0;top:2690px;width:1200px;height:300px;background:var(--sky);border-top:1px solid #d3e4f2}
.review{display:flex;gap:16px;height:86px}
.avatar{width:72px;height:72px;flex:none}
.r-title{font-weight:700;color:var(--blue);font-size:13px;display:flex;justify-content:space-between}
.pill{font-size:10px;font-weight:400;color:#fff;background:#7aa3c9;padding:0 8px;border-radius:9px;line-height:18px}
.r-text{font-size:12px;color:#5c646d;line-height:18px;margin:4px 0}
.report{font-size:11px;color:var(--orange)}

/* footer */
.footer{left:0;top:2990px;width:1200px;height:376px;background:var(--foot);color:#b8bec5}
.f-col h4{color:#fff;font-size:14px;font-weight:700;margin-bottom:16px}
.f-list{list-style:none}
.f-list li{font-size:12px;line-height:24px}
.f-input{width:220px;height:30px;background:#fff;color:#999;font-size:11px;line-height:30px;padding:0 10px;border-radius:2px}
.copy{left:0;top:3366px;width:1200px;height:30px;background:var(--foot-2);color:#7d848c;font-size:11px;line-height:30px;padding-left:112px}
</style>
</head>
<body>

<header class="abs header">
  <div class="abs brand"><div class="brand-name">Divora</div><div class="brand-sub">Diving Center</div></div>
  <div class="abs top-actions">
    <span class="btn-top primary">Sign in</span><span class="btn-top">Join</span><span class="btn-top">Language ▾</span>
  </div>
  <nav class="abs nav">
    <a class="active">Home</a><a>Latest</a><a>Photo</a><a>Videos</a><a>Fauna</a><a>Dive Site</a><a>Dive Center</a><a>Divers</a><a>Forum</a>
  </nav>
</header>
<div class="abs wrap hero" role="img" aria-label="Diver swimming beside yellow coral in clear blue water"></div>

<!-- main information -->
<section class="abs" style="left:112px;top:630px;width:470px">
  <div style="display:flex;justify-content:space-between;align-items:center;height:30px"><span class="sec-title">Main Information</span><span class="like"><i></i>Like</span></div>
  <div class="rule" style="margin:8px 0 18px"></div>
  <div style="display:flex;gap:22px">
    <div class="photo" style="width:110px;height:130px;background:linear-gradient(#7cc6e4,#2a86b8)" role="img" aria-label="Dive center portrait"></div>
    <div class="info-grid">
      <div class="info-row"><span class="label">Location:</span>Indonesia Bali</div>
      <div class="info-row"><span class="label">Affiliation:</span><a>NAVRO</a></div>
      <div class="info-row"><span class="label">Active Since:</span>2006</div>
      <div class="info-row"><span class="label">Location:</span>
        <span class="flag" style="background:linear-gradient(#c8102e 50%,#fff 50%)"></span><span class="flag" style="background:linear-gradient(#1c3d8c 34%,#fff 34%,#fff 66%,#c8102e 66%)"></span><span class="flag" style="background:linear-gradient(90deg,#0a8a3c 33%,#fff 33%,#fff 66%,#d0202a 66%)"></span></div>
    </div>
  </div>
  <div style="text-align:right;margin-top:14px"><span class="btn">Write a Review</span></div>
</section>

<section class="abs" style="left:618px;top:630px;width:470px">
  <div style="display:flex;justify-content:space-between;align-items:center;height:30px"><span class="sec-title">Rating <small>(15 Votes)</small></span><span class="like"><i></i>Like</span></div>
  <div class="rule" style="margin:8px 0 18px"></div>
  <div style="display:flex;gap:22px">
    <div class="photo" style="width:110px;height:130px;background:linear-gradient(#5fb6d8,#1b6a9c)" role="img" aria-label="Diver portrait underwater"></div>
    <div style="flex:1">
      <div class="rate-row"><span>Professionalism</span><span class="stars"><svg width="80" height="14"><g fill="var(--star)"><path id="s" d="M7 0l2 4.6 5 .5-3.8 3.3 1.1 4.9L7 10.8 2.7 13.3l1.1-4.9L0 5.1l5-.5z"/><use href="#s" x="16"/><use href="#s" x="32"/><use href="#s" x="48"/><use href="#s" x="64"/></g></svg></span></div>
      <div class="rate-row"><span>Safety</span><span class="stars"><svg width="80" height="14"><g fill="var(--star)"><use href="#s"/><use href="#s" x="16"/><use href="#s" x="32"/><use href="#s" x="48"/></g><use href="#s" x="64" fill="#d5d9de"/></svg></span></div>
      <div class="rate-row"><span>Equipment Air Quality</span><span class="stars"><svg width="80" height="14"><g fill="var(--star)"><use href="#s"/><use href="#s" x="16"/><use href="#s" x="32"/><use href="#s" x="48"/><use href="#s" x="64"/></g></svg></span></div>
      <div class="rate-row"><span>Friendliness</span><span class="stars"><svg width="80" height="14"><g fill="var(--star)"><use href="#s"/><use href="#s" x="16"/><use href="#s" x="32"/><use href="#s" x="48"/></g><use href="#s" x="64" fill="#d5d9de"/></svg></span></div>
      <div class="rate-row"><span>Price for the Services</span><span class="stars"><svg width="80" height="14"><g fill="var(--star)"><use href="#s"/><use href="#s" x="16"/><use href="#s" x="32"/></g><g fill="#d5d9de"><use href="#s" x="48"/><use href="#s" x="64"/></g></svg></span></div>
    </div>
  </div>
  <div style="text-align:right;margin-top:8px"><span class="btn">Write a Review</span></div>
</section>

<!-- facilities -->
<section class="abs wrap" style="top:960px">
  <div class="sec-title" style="height:30px">Facilities</div>
  <div class="rule" style="margin:8px 0 14px"></div>
  <div style="display:flex">
    <ul class="fac-list" style="width:325px"><li>Accomodation</li><li>Photo of Your Dive</li><li>Own Boat</li><li>Rental Gear</li><li>Nitrox</li><li>Swimming Pool</li></ul>
    <ul class="fac-list" style="width:325px"><li>Up to 4 Divers Per Guide</li><li>Technical Dive</li><li>Trimix</li><li>Compressor</li><li>Shop</li><li>Rebreather</li></ul>
    <ul class="fac-list" style="width:325px"><li>Restauration</li><li>Accomodation on Site</li><li>Accomodation off Site</li><li>Photography Gear Rental</li><li>Oxygen on Board</li></ul>
  </div>
  <div class="rule" style="margin-top:18px"></div>
</section>

<!-- gallery -->
<section class="abs wrap" style="top:1270px">
  <div class="tabs"><span class="tab active">Play Slideshow</span><span class="tab">Our Team</span><span class="tab">Prizes</span><span class="tab">Photo Gallery</span><span class="tab">Video Gallery</span></div>
</section>
<div class="abs wrap" style="top:1330px;display:grid;grid-template-columns:repeat(3,304px);column-gap:32px;row-gap:30px">
  <article class="g-card"><div class="photo" style="background:linear-gradient(#3da7d8,#0f5f96)" role="img" aria-label="Diver over the reef"></div><div class="meta"><span>● Stelian Kostov</span><span>12 Views</span></div><div class="g-title">Lorem Ipsum is simply dummy text</div><div class="g-text">Lorem Ipsum is simply dummy text of the printing and typesetting industry.</div></article>
  <article class="g-card"><div class="photo" style="background:linear-gradient(#9fd3ea,#2a8fc0)" role="img" aria-label="Two divers at the surface"></div><div class="meta"><span>● Mira Delcourt</span><span>9 Views</span></div><div class="g-title">Lorem Ipsum is simply dummy text</div><div class="g-text">Lorem Ipsum is simply dummy text of the printing and typesetting industry.</div></article>
  <article class="g-card"><div class="photo" style="background:linear-gradient(#57b9e0,#156ea4)" role="img" aria-label="Diver near coral"></div><div class="meta"><span>● Tomas Renn</span><span>15 Views</span></div><div class="g-title">Lorem Ipsum is simply dummy text</div><div class="g-text">Lorem Ipsum is simply dummy text of the printing and typesetting industry.</div></article>
  <article class="g-card"><div class="photo" style="background:linear-gradient(#bfe8f2,#4fb0cc)" role="img" aria-label="Beach and shallow lagoon"></div><div class="meta"><span>● Aline Moreau</span><span>7 Views</span></div><div class="g-title">Lorem Ipsum is simply dummy text</div><div class="g-text">Lorem Ipsum is simply dummy text of the printing and typesetting industry.</div></article>
  <article class="g-card"><div class="photo" style="background:linear-gradient(#2a93b0,#0c4e6e)" role="img" aria-label="Sea turtle swimming"></div><div class="meta"><span>● Kai Lindholm</span><span>21 Views</span></div><div class="g-title">Lorem Ipsum is simply dummy text</div><div class="g-text">Lorem Ipsum is simply dummy text of the printing and typesetting industry.</div></article>
  <article class="g-card"><div class="photo" style="background:linear-gradient(#a9def0,#3e9fcc)" role="img" aria-label="Divers on the beach"></div><div class="meta"><span>● Rosa Ibarra</span><span>11 Views</span></div><div class="g-title">Lorem Ipsum is simply dummy text</div><div class="g-text">Lorem Ipsum is simply dummy text of the printing and typesetting industry.</div></article>
</div>
<div class="abs wrap" style="top:2040px;text-align:center"><span class="btn">Show More</span></div>

<!-- neighbouring sites -->
<section class="abs wrap" style="top:2120px">
  <div style="display:flex;justify-content:space-between;align-items:center;height:30px"><span class="sec-title">Neighbouring Dive Site (6)</span><span class="link">See All Dive Sites (6)</span></div>
  <div class="rule" style="margin-top:8px"></div>
</section>
<div class="abs wrap" style="top:2180px;display:grid;grid-template-columns:470px 470px;column-gap:36px;row-gap:24px">
  <div class="site"><div class="photo" style="background:linear-gradient(#6ec3e2,#1d77a8)" role="img" aria-label="Diver at Nusa Penida"></div><div><div class="site-name">Nusa Penida</div><div class="site-row"><b>Rating:</b>★★★★☆ <span style="color:var(--muted);font-size:10px">(3 Votes)</span></div><div class="site-row"><b>Distance:</b>19.66km</div><div class="site-row"><b>Comments:</b>0</div><div class="site-row"><b>Photo:</b>0</div><div class="site-row"><b>Video:</b>0</div></div></div>
  <div class="site"><div class="photo" style="background:linear-gradient(#4fb0d6,#145f93)" role="img" aria-label="Divers at Blue Lagoon"></div><div><div class="site-name">Blue Lagoon</div><div class="site-row"><b>Rating:</b>★★★★☆ <span style="color:var(--muted);font-size:10px">(3 Votes)</span></div><div class="site-row"><b>Distance:</b>19.66km</div><div class="site-row"><b>Comments:</b>0</div><div class="site-row"><b>Photo:</b>0</div><div class="site-row"><b>Video:</b>0</div></div></div>
  <div class="site"><div class="photo" style="background:linear-gradient(#8fd0e6,#2f87b4)" role="img" aria-label="Diver at White Sand Beach"></div><div><div class="site-name">White Sand Beach</div><div class="site-row"><b>Rating:</b>★★★★☆ <span style="color:var(--muted);font-size:10px">(3 Votes)</span></div><div class="site-row"><b>Distance:</b>19.66km</div><div class="site-row"><b>Comments:</b>0</div><div class="site-row"><b>Photo:</b>0</div><div class="site-row"><b>Video:</b>0</div></div></div>
  <div class="site"><div class="photo" style="background:linear-gradient(#3d9fc8,#0f4f7e)" role="img" aria-label="Diver in the channel"></div><div><div class="site-name">Channel</div><div class="site-row"><b>Rating:</b>★★★★☆ <span style="color:var(--muted);font-size:10px">(3 Votes)</span></div><div class="site-row"><b>Distance:</b>19.66km</div><div class="site-row"><b>Comments:</b>0</div><div class="site-row"><b>Photo:</b>0</div><div class="site-row"><b>Video:</b>0</div></div></div>
</div>

<!-- reviews -->
<section class="abs reviews">
  <div class="abs wrap" style="top:20px">
    <div style="display:flex;justify-content:space-between;align-items:center;height:30px"><span class="sec-title">Reviews(1)</span><span class="link">Show the reviews</span></div>
    <div class="rule" style="margin:6px 0 14px;background:#cddfee"></div>
    <div class="review"><div class="avatar photo" style="background:linear-gradient(#f0a64a,#c0701c)" role="img" aria-label="Reviewer avatar"></div><div style="flex:1"><div class="r-title">This is Perfect....<span class="pill">12 Jan 2014</span></div><div class="r-text">Lorem Ipsum is simply dummy text of the printing and typesetting industry. Lorem Ipsum has been the industry's standard dummy text ever since the 1500s, when an unknown printer took a galley of type and scrambled it.</div><div class="report">[Report a Problem]</div></div></div>
    <div class="review"><div class="avatar photo" style="background:linear-gradient(#f0a64a,#c0701c)" role="img" aria-label="Reviewer avatar"></div><div style="flex:1"><div class="r-title">This is Perfect....<span class="pill">12 Jan 2014</span></div><div class="r-text">Lorem Ipsum is simply dummy text of the printing and typesetting industry. Lorem Ipsum has been the industry's standard dummy text ever since the 1500s, when an unknown printer took a galley of type and scrambled it.</div><div class="report">[Report a Problem]</div></div></div>
    <div style="padding-left:88px;margin-top:4px"><span class="btn">Write a Review</span></div>
  </div>
</section>

<!-- footer -->
<footer class="abs footer">
  <div class="abs wrap" style="top:40px;display:flex">
    <div class="f-col" style="width:250px"><h4>Quick Links</h4><div style="display:flex;gap:40px"><ul class="f-list"><li>Home</li><li>Latest</li><li>Photo</li><li>Videos</li><li>Fauna</li></ul><ul class="f-list"><li>Dive Site</li><li>Dive Center</li><li>Divers</li><li>Forum</li></ul></div></div>
    <div class="f-col" style="width:250px"><h4>Contact Info</h4><ul class="f-list"><li>Divora Center, Harbour Lane 12</li><li>Sanur 80228, Bali, Indonesia</li><li>Phone: +62 361 555 0142</li><li>Email: hello@divora-dive.net</li></ul></div>
    <div class="f-col" style="width:270px"><h4>Newsletter</h4><div class="f-input">Enter Your Email</div><div class="btn" style="margin-top:10px;height:28px;line-height:28px">SUBSCRIBE</div><div style="margin-top:14px"><span class="like"><i></i>Like</span> <span style="font-size:11px">742 people like this.</span></div></div>
    <div class="f-col" style="width:206px"><h4>Best Contributors</h4><div style="display:flex;gap:16px"><div><div class="photo" style="width:64px;height:64px;background:linear-gradient(#6ec3e2,#1d77a8)" role="img" aria-label="Contributor photo"></div><div style="font-size:11px;margin-top:6px">Julien</div></div><div><div class="photo" style="width:64px;height:64px;background:linear-gradient(#4fb0d6,#145f93)" role="img" aria-label="Contributor photo"></div><div style="font-size:11px;margin-top:6px">Marco Dean</div></div></div></div>
  </div>
</footer>
<div class="abs copy">Copyright © 2014 Divora Diving Center. All rights reserved.</div>

</body>
</html>
```